Wix Web design for a Residential redevelopment company

I need a website with a modern and elegant feel that will attract investors. I would like for the color scale to include the colors in our logo and also shades of grey for a modern feel. I need a page for property case studies in which each case study includes property before and after photos, an imbeded youtube video and text in the format of a math problem showing the amount the property was bought for -(minus) what the investor got in return -(minus) rehab costs -(minus) taxes and fees =(equals) Net Profit
However instead of there being an equal sign, I want the math problem to go vertically down with an underline for the equals sign.There needs to be an "About us," page, Investor Inquiries page, Contact Us Page, and Case studies page.
For font formatting, we like Corporate Gothic. Please make the website Wix friendly.

When someone clicks on one of the case study pictures, I would like the pictures to pull up in a click or swipe to the right manner similar to how pictures are structured on mebrank or pendosa.com

Target Market(s)

Investors

Industry/Entity Type

Real Estate

Number of Pages Required

5+ page

Font styles to use
Other font styles liked:
• Gothic Corporate

Requirements
Nice to have
• stock photos for the home page

```html
<!DOCTYPE html>
<html lang="en">
<head>
<meta charset="utf-8">
<title>Halvern Homes</title>
<link rel="stylesheet" href="https://fonts.googleapis.com/css2?family=Questrial&family=Open+Sans:wght@400;600&display=swap">
<style>
:root{
  --green:#4aa33a;
  --green-dark:#3b8a2d;
  --blue:#1e63c6;
  --blue-dark:#134f9f;
  --ink:#2b2b2b;
  --grey-bg:#f3f3f3;
  --line:#e3e3e3;
  --muted:#666;
  --white:#fff;
}
*{box-sizing:border-box;margin:0;padding:0}
html,body{width:1200px;height:2161px;overflow:hidden}
body{position:relative;background:var(--grey-bg);font-family:"Open Sans",sans-serif;color:var(--ink)}
.abs{position:absolute}

/* hero */
.hero{left:0;top:0;width:1200px;height:527px;background:linear-gradient(180deg,#9cb7d4 0%,#c9d3d8 30%,#d9c7a4 60%,#5d6f3f 100%)}
.logo-box{left:144px;top:0;width:111px;height:115px;background:var(--white);display:flex;align-items:center;justify-content:center;flex-direction:column;gap:6px}
.logo-box .mark{width:26px;height:26px;border-radius:50%;background:var(--green)}
.logo-box .name{font-family:"Questrial",sans-serif;font-size:14px;color:var(--blue);letter-spacing:.5px}
.main-nav{left:420px;top:51px;display:flex;gap:24px;font-family:"Questrial",sans-serif;font-size:10px;color:var(--white);letter-spacing:.4px;white-space:nowrap}
.btn-login,.btn-register{top:45px;height:25px;font-family:"Questrial",sans-serif;font-size:10px;color:var(--white);display:flex;align-items:center;justify-content:center}
.btn-login{left:887px;width:72px;background:var(--blue)}
.btn-register{left:967px;width:89px;background:var(--green)}
.search-tabs{left:222px;top:244px;display:flex;font-family:"Questrial",sans-serif;font-size:13px;color:var(--white)}
.search-tabs span{height:30px;display:flex;align-items:center;justify-content:center}
.tab-buy{width:120px;background:var(--green)}
.tab-rent{width:121px;background:var(--blue);border-left:1px solid #4a86da}
.tab-sold{width:120px;background:var(--blue);border-left:1px solid #4a86da}
.search-panel{left:222px;top:274px;width:750px;height:59px;background:var(--white)}
.search-input{left:23px;top:14px;width:601px;height:32px;border:1px solid #d4d4d4;font-family:"Questrial",sans-serif;font-size:11px;color:#999;padding-left:10px;display:flex;align-items:center;letter-spacing:.4px}
.search-btn{left:638px;top:13px;width:95px;height:33px;background:var(--green);color:var(--white);font-family:"Questrial",sans-serif;font-size:11px;display:flex;align-items:center;justify-content:center;letter-spacing:.5px}
.advanced{left:222px;top:333px;width:176px;height:30px;background:var(--green);color:var(--white);font-family:"Questrial",sans-serif;font-size:10px;display:flex;align-items:center;gap:10px;padding-left:20px;letter-spacing:.4px}
.arrow{width:40px;height:40px}

/* listing sections */
.section-title{left:0;width:1200px;text-align:center;font-family:"Questrial",sans-serif;font-size:25px;font-weight:400;letter-spacing:1.5px;color:var(--ink);-webkit-text-stroke:.5px var(--ink)}
.title-rule{left:574px;width:52px;height:2px;background:var(--green)}
.listing-row{left:0;width:1200px;display:grid;grid-template-columns:repeat(4,300px)}
.listing-card{position:relative}
.listing-photo{height:200px}
.photo-a{background:linear-gradient(180deg,#3f8fd6 0%,#2d5c9a 55%,#6aa342 100%)}
.photo-b{background:linear-gradient(180deg,#6fa6d8 0%,#b7c4b2 45%,#4f8f36 100%)}
.photo-c{background:linear-gradient(180deg,#9fb9cf 0%,#a7967a 50%,#4d7d30 100%)}
.photo-d{background:linear-gradient(180deg,#4e90d2 0%,#c9ccd2 50%,#5c9b3a 100%)}
.roi-badge{position:absolute;left:0;top:168px;display:flex;font-family:"Open Sans",sans-serif;font-size:16px;color:var(--white)}
.roi-badge span{height:32px;width:52px;display:flex;align-items:center;justify-content:center}
.roi-pct{background:#111}
.roi-label{background:var(--green)}
.listing-info{display:grid;grid-template-columns:150px 150px;height:32px;background:var(--white)}
.listing-info div{display:flex;align-items:center;gap:8px;padding-left:16px;font-size:9px;color:var(--muted);border-right:1px solid var(--line)}
.row-arrow{width:40px;height:40px}

/* contact band */
.contact-band{left:0;top:1693px;width:1200px;height:158px;background:linear-gradient(90deg,#e6e8e4,#eef0ec 50%,#e4e7e2)}
.contact-title{left:179px;top:54px;font-family:"Questrial",sans-serif;font-size:21px;font-weight:400;color:#111;letter-spacing:.5px;-webkit-text-stroke:.3px #111}
.contact-text{left:179px;top:83px;font-size:12px;color:#444}
.phone-btn{left:827px;top:60px;width:194px;height:39px;background:var(--blue);border:1px solid var(--blue-dark);color:var(--white);font-family:"Questrial",sans-serif;font-size:19px;display:flex;align-items:center;justify-content:center;letter-spacing:.5px}

/* footer */
.site-footer{left:0;top:1851px;width:1200px;height:310px;background:var(--white)}
.footer-col{top:54px;width:210px}
.footer-col h4{font-family:"Open Sans",sans-serif;font-weight:600;font-size:11px;color:var(--green);margin-bottom:13px}
.footer-col li{list-style:none;font-size:10px;color:#333;line-height:22.3px}
.footer-col li.more{color:var(--green)}
.footer-rule{left:144px;top:238px;width:912px;height:1px;background:var(--line)}
.copyright{left:144px;top:260px;font-size:9px;color:#555}
.social{top:257px;width:23px;height:23px;border-radius:50%}
</style>
</head>
<body>

<header class="abs hero" role="img" aria-label="Photo of a two-storey cream suburban house with trees under a blue sky"></header>
<div class="abs logo-box"><span class="mark"></span><span class="name">Halvern Homes</span></div>
<nav class="abs main-nav"><span>HOME</span><span>ABOUT US</span><span>CASE STUDIES</span><span>INVESTOR INQUIRIES</span><span>CONTACT US</span></nav>
<div class="abs btn-login">LOGIN</div>
<div class="abs btn-register">REGISTER</div>

<svg class="abs arrow" style="left:143px;top:284px" viewBox="0 0 40 40"><circle cx="20" cy="20" r="18" fill="none" stroke="#fff" stroke-width="2"/><path d="M23 12 L15 20 L23 28" fill="none" stroke="#fff" stroke-width="2"/></svg>
<svg class="abs arrow" style="left:1015px;top:284px" viewBox="0 0 40 40"><circle cx="20" cy="20" r="18" fill="none" stroke="#fff" stroke-width="2"/><path d="M17 12 L25 20 L17 28" fill="none" stroke="#fff" stroke-width="2"/></svg>

<div class="abs search-tabs"><span class="tab-buy">BUY</span><span class="tab-rent">RENT</span><span class="tab-sold">SOLD</span></div>
<div class="abs search-panel">
  <div class="abs search-input">CITY, STATE, ZIP CODE</div>
  <div class="abs search-btn">SEARCH</div>
</div>
<div class="abs advanced">ADVANCED SEARCH
  <svg width="16" height="16" viewBox="0 0 16 16"><circle cx="8" cy="8" r="7" fill="none" stroke="#fff" stroke-width="1.3"/><path d="M7 5 L10 8 L7 11" fill="none" stroke="#fff" stroke-width="1.3"/></svg>
</div>

<!-- Recently added -->
<h2 class="abs section-title" style="top:572px">RECENTLY ADDED</h2>
<div class="abs title-rule" style="top:613px"></div>
<section class="abs listing-row" style="top:653px">
  <article class="listing-card"><div class="listing-photo photo-a" role="img" aria-label="Photo of a blue two-storey house"></div><div class="roi-badge"><span class="roi-pct">50%</span><span class="roi-label">ROI</span></div><div class="listing-info"><div><svg width="12" height="8"><rect y="2" width="12" height="4" fill="#4aa33a"/><rect width="2" height="8" fill="#4aa33a"/></svg>3 Bedroom</div><div><svg width="10" height="10"><circle cx="5" cy="5" r="5" fill="#4aa33a"/></svg>2 Bathroom</div></div></article>
  <article class="listing-card"><div class="listing-photo photo-b" role="img" aria-label="Photo of a grey-green house with garden"></div><div class="roi-badge"><span class="roi-pct">50%</span><span class="roi-label">ROI</span></div><div class="listing-info"><div><svg width="12" height="8"><rect y="2" width="12" height="4" fill="#4aa33a"/><rect width="2" height="8" fill="#4aa33a"/></svg>3 Bedroom</div><div><svg width="10" height="10"><circle cx="5" cy="5" r="5" fill="#4aa33a"/></svg>2 Bathroom</div></div></article>
  <article class="listing-card"><div class="listing-photo photo-c" role="img" aria-label="Photo of a stone and beige family house"></div><div class="roi-badge"><span class="roi-pct">50%</span><span class="roi-label">ROI</span></div><div class="listing-info"><div><svg width="12" height="8"><rect y="2" width="12" height="4" fill="#4aa33a"/><rect width="2" height="8" fill="#4aa33a"/></svg>3 Bedroom</div><div><svg width="10" height="10"><circle cx="5" cy="5" r="5" fill="#4aa33a"/></svg>2 Bathroom</div></div></article>
  <article class="listing-card"><div class="listing-photo photo-d" role="img" aria-label="Photo of a white house with double garage"></div><div class="roi-badge"><span class="roi-pct">50%</span><span class="roi-label">ROI</span></div><div class="listing-info"><div><svg width="12" height="8"><rect y="2" width="12" height="4" fill="#4aa33a"/><rect width="2" height="8" fill="#4aa33a"/></svg>3 Bedroom</div><div><svg width="10" height="10"><circle cx="5" cy="5" r="5" fill="#4aa33a"/></svg>2 Bathroom</div></div></article>
</section>
<svg class="abs row-arrow" style="left:23px;top:733px" viewBox="0 0 40 40"><circle cx="20" cy="20" r="18" fill="rgba(0,0,0,.25)" stroke="#fff" stroke-width="2"/><path d="M23 12 L15 20 L23 28" fill="none" stroke="#fff" stroke-width="2"/></svg>
<svg class="abs row-arrow" style="left:1136px;top:733px" viewBox="0 0 40 40"><circle cx="20" cy="20" r="18" fill="rgba(0,0,0,.25)" stroke="#fff" stroke-width="2"/><path d="M17 12 L25 20 L17 28" fill="none" stroke="#fff" stroke-width="2"/></svg>

<!-- For sell -->
<h2 class="abs section-title" style="top:932px">FOR SELL</h2>
<div class="abs title-rule" style="top:973px"></div>
<section class="abs listing-row" style="top:1013px">
  <article class="listing-card"><div class="listing-photo photo-a" role="img" aria-label="Photo of a blue two-storey house"></div><div class="roi-badge"><span class="roi-pct">50%</span><span class="roi-label">ROI</span></div><div class="listing-info"><div><svg width="12" height="8"><rect y="2" width="12" height="4" fill="#4aa33a"/><rect width="2" height="8" fill="#4aa33a"/></svg>3 Bedroom</div><div><svg width="10" height="10"><circle cx="5" cy="5" r="5" fill="#4aa33a"/></svg>2 Bathroom</div></div></article>
  <article class="listing-card"><div class="listing-photo photo-b" role="img" aria-label="Photo of a grey-green house with garden"></div><div class="roi-badge"><span class="roi-pct">50%</span><span class="roi-label">ROI</span></div><div class="listing-info"><div><svg width="12" height="8"><rect y="2" width="12" height="4" fill="#4aa33a"/><rect width="2" height="8" fill="#4aa33a"/></svg>3 Bedroom</div><div><svg width="10" height="10"><circle cx="5" cy="5" r="5" fill="#4aa33a"/></svg>2 Bathroom</div></div></article>
  <article class="listing-card"><div class="listing-photo photo-c" role="img" aria-label="Photo of a stone and beige family house"></div><div class="roi-badge"><span class="roi-pct">50%</span><span class="roi-label">ROI</span></div><div class="listing-info"><div><svg width="12" height="8"><rect y="2" width="12" height="4" fill="#4aa33a"/><rect width="2" height="8" fill="#4aa33a"/></svg>3 Bedroom</div><div><svg width="10" height="10"><circle cx="5" cy="5" r="5" fill="#4aa33a"/></svg>2 Bathroom</div></div></article>
  <article class="listing-card"><div class="listing-photo photo-d" role="img" aria-label="Photo of a white house with double garage"></div><div class="roi-badge"><span class="roi-pct">50%</span><span class="roi-label">ROI</span></div><div class="listing-info"><div><svg width="12" height="8"><rect y="2" width="12" height="4" fill="#4aa33a"/><rect width="2" height="8" fill="#4aa33a"/></svg>3 Bedroom</div><div><svg width="10" height="10"><circle cx="5" cy="5" r="5" fill="#4aa33a"/></svg>2 Bathroom</div></div></article>
</section>
<svg class="abs row-arrow" style="left:23px;top:1093px" viewBox="0 0 40 40"><circle cx="20" cy="20" r="18" fill="rgba(0,0,0,.25)" stroke="#fff" stroke-width="2"/><path d="M23 12 L15 20 L23 28" fill="none" stroke="#fff" stroke-width="2"/></svg>
<svg class="abs row-arrow" style="left:1136px;top:1093px" viewBox="0 0 40 40"><circle cx="20" cy="20" r="18" fill="rgba(0,0,0,.25)" stroke="#fff" stroke-width="2"/><path d="M17 12 L25 20 L17 28" fill="none" stroke="#fff" stroke-width="2"/></svg>

<!-- For rent -->
<h2 class="abs section-title" style="top:1291px">FOR RENT</h2>
<div class="abs title-rule" style="top:1332px"></div>
<section class="abs listing-row" style="top:1372px">
  <article class="listing-card"><div class="listing-photo photo-a" role="img" aria-label="Photo of a blue two-storey house"></div><div class="roi-badge"><span class="roi-pct">50%</span><span class="roi-label">ROI</span></div><div class="listing-info"><div><svg width="12" height="8"><rect y="2" width="12" height="4" fill="#4aa33a"/><rect width="2" height="8" fill="#4aa33a"/></svg>3 Bedroom</div><div><svg width="10" height="10"><circle cx="5" cy="5" r="5" fill="#4aa33a"/></svg>2 Bathroom</div></div></article>
  <article class="listing-card"><div class="listing-photo photo-b" role="img" aria-label="Photo of a grey-green house with garden"></div><div class="roi-badge"><span class="roi-pct">50%</span><span class="roi-label">ROI</span></div><div class="listing-info"><div><svg width="12" height="8"><rect y="2" width="12" height="4" fill="#4aa33a"/><rect width="2" height="8" fill="#4aa33a"/></svg>3 Bedroom</div><div><svg width="10" height="10"><circle cx="5" cy="5" r="5" fill="#4aa33a"/></svg>2 Bathroom</div></div></article>
  <article class="listing-card"><div class="listing-photo photo-c" role="img" aria-label="Photo of a stone and beige family house"></div><div class="roi-badge"><span class="roi-pct">50%</span><span class="roi-label">ROI</span></div><div class="listing-info"><div><svg width="12" height="8"><rect y="2" width="12" height="4" fill="#4aa33a"/><rect width="2" height="8" fill="#4aa33a"/></svg>3 Bedroom</div><div><svg width="10" height="10"><circle cx="5" cy="5" r="5" fill="#4aa33a"/></svg>2 Bathroom</div></div></article>
  <article class="listing-card"><div class="listing-photo photo-d" role="img" aria-label="Photo of a white house with double garage"></div><div class="roi-badge"><span class="roi-pct">50%</span><span class="roi-label">ROI</span></div><div class="listing-info"><div><svg width="12" height="8"><rect y="2" width="12" height="4" fill="#4aa33a"/><rect width="2" height="8" fill="#4aa33a"/></svg>3 Bedroom</div><div><svg width="10" height="10"><circle cx="5" cy="5" r="5" fill="#4aa33a"/></svg>2 Bathroom</div></div></article>
</section>
<svg class="abs row-arrow" style="left:23px;top:1452px" viewBox="0 0 40 40"><circle cx="20" cy="20" r="18" fill="rgba(0,0,0,.25)" stroke="#fff" stroke-width="2"/><path d="M23 12 L15 20 L23 28" fill="none" stroke="#fff" stroke-width="2"/></svg>
<svg class="abs row-arrow" style="left:1136px;top:1452px" viewBox="0 0 40 40"><circle cx="20" cy="20" r="18" fill="rgba(0,0,0,.25)" stroke="#fff" stroke-width="2"/><path d="M17 12 L25 20 L17 28" fill="none" stroke="#fff" stroke-width="2"/></svg>

<!-- Contact band -->
<section class="abs contact-band">
  <h3 class="abs contact-title">CONTACT US FOR MORE INFORMATION</h3>
  <p class="abs contact-text">Aenean eu leo quam. Pellentesque ornare sem lacinia quam venenatis vestibulum.</p>
  <div class="abs phone-btn">014-2867-350</div>
</section>

<!-- Footer -->
<footer class="abs site-footer">
  <div class="abs footer-col" style="left:144px"><h4>Real Estate</h4><ul><li>Browse all homes</li><li>Albuquerque real estate</li><li>Atlanta real estate</li><li>Austin real estate</li><li>Baltimore real estate</li><li class="more">more</li></ul></div>
  <div class="abs footer-col" style="left:377px"><h4>Rentals</h4><ul><li>Rental Buildings</li><li>Atlanta apartments for rent</li><li>Austin apartments for rent</li><li>Baltimore apartments for rent</li><li>Boston apartments for rent</li><li class="more">more</li></ul></div>
  <div class="abs footer-col" style="left:612px"><h4>Mortgage Rates</h4><ul><li>Current mortgage rates</li><li>Alaska mortgage rates</li><li>Alabama mortgage rates</li><li>Arkansas mortgage rates</li><li>Arizona mortgage rates</li><li class="more">more</li></ul></div>
  <div class="abs footer-col" style="left:847px"><h4>Browse Home</h4><ul><li>California</li><li>Texas</li><li>New York</li><li>Florida</li><li>Illinois</li><li class="more">more</li></ul></div>
  <div class="abs footer-rule"></div>
  <p class="abs copyright">All rights reserved 2016.</p>
  <span class="abs social" style="left:967px;background:#4a9fe0"></span>
  <span class="abs social" style="left:998px;background:#3b5ba0"></span>
  <span class="abs social" style="left:1030px;background:#3f7fb8"></span>
</footer>

</body>
</html>
```